Post storm repair flyer

looking for an eye catching 6x9 postcard to send out to single family home owners advertising a "Post Storm Repair Special" explaining that after the recent hurricanes its very important to have your roof checked and any repairs fixed right away before they become a bigger more costly problem and that even though your home wasn't directly hit by the storm the high wind gust could've cause unseen damage.
offer $200 off any repair *some rules may apply
Lark Roofing
888.417.LARK
www.LarkRoofing.example

Roofing

```html
<!DOCTYPE html>
<html lang="en">
<head>
<meta charset="utf-8">
<title>Lark Roofing – Post Storm Repair Special Postcard</title>
<link href="https://fonts.googleapis.com/css2?family=Bebas+Neue&family=Jost:wght@500;600&family=Montserrat:wght@500&family=Oswald:wght@600&display=swap" rel="stylesheet">
<style>
  :root {
    --backdrop: #fdb94f;
    --ink: #1a1a1a;
    --paper: #ffffff;
    --accent: #fdb913;
    --rule: #9a9a9a;
    --photo-sky: #c9d2da;
    --photo-roof: #5d6166;
  }
  * { margin: 0; padding: 0; box-sizing: border-box; }
  html, body { width: 1200px; height: 948px; overflow: hidden; }
  body { background: var(--backdrop); position: relative; font-family: "Montserrat", sans-serif; }

  .postcard {
    position: absolute; top: 69px; width: 538px; height: 808px; overflow: hidden;
    box-shadow: 0 10px 22px rgba(0,0,0,.28);
  }
  .postcard--front { left: 48px; background: var(--ink); }
  .postcard--back { left: 612px; background: var(--paper); }

  .hero-photo {
    position: absolute; left: 0; top: 0; width: 538px; height: 420px;
    background: linear-gradient(160deg, var(--photo-sky) 0%, #9aa3ab 35%, var(--photo-roof) 75%, #3d4044 100%);
  }
  .shape { position: absolute; left: 0; top: 0; }

  .brand-mark {
    position: absolute; left: 0; width: 538px; text-align: center;
    font-family: "Jost", sans-serif; font-weight: 600; color: var(--paper);
    letter-spacing: .5px;
  }
  .brand-mark .dot {
    display: block; margin: 0 auto 14px; background: var(--accent);
  }
  .postcard--front .brand-mark { top: 230px; font-size: 31px; }
  .postcard--front .brand-mark .dot { width: 26px; height: 26px; }
  .postcard--back .brand-mark { top: 86px; font-size: 36px; }
  .postcard--back .brand-mark .dot { width: 30px; height: 30px; margin-bottom: 20px; }

  .headline {
    position: absolute; left: 0; width: 538px; text-align: center;
    font-family: "Bebas Neue", "Oswald", sans-serif; line-height: 1;
  }
  .headline--top { top: 348px; font-size: 74px; color: var(--accent); }
  .headline--bottom { top: 414px; font-size: 76px; color: var(--paper); }

  .damage-photos { position: absolute; left: 55px; top: 491px; display: flex; gap: 4px; }
  .damage-photos span {
    width: 140px; height: 89px; border: 1.5px solid var(--paper); border-radius: 6px;
  }
  .damage-photos .p1 { background: linear-gradient(135deg, #6e7378, #a9a79d 45%, #5a5f64); }
  .damage-photos .p2 { background: linear-gradient(160deg, #d9dcdf 0%, #c3c6c9 25%, #4b4f54 55%, #2f3236); }
  .damage-photos .p3 { background: linear-gradient(120deg, #3a3d41 0%, #6b6f73 40%, #b9a58e 65%, #9aa0a6); }

  .accent-rule { position: absolute; height: 2px; background: var(--accent); border-radius: 1px; }
  .postcard--front .accent-rule { left: 168px; top: 596px; width: 202px; }
  .postcard--back .accent-rule { left: 152px; top: 377px; width: 234px; }

  .body-copy {
    position: absolute; left: 0; width: 538px; text-align: center; color: var(--paper);
    font-weight: 500;
  }
  .postcard--front .body-copy { top: 613px; font-size: 15.3px; line-height: 20px; }
  .postcard--back .body-copy { top: 234px; font-size: 24px; line-height: 31px; letter-spacing: .3px; }

  .contact { position: absolute; left: 28px; top: 733px; font-family: "Jost", sans-serif; }
  .contact .name { font-size: 21px; font-weight: 500; line-height: 20px; letter-spacing: .3px; }
  .contact .phone {
    font-family: "Oswald", sans-serif; font-weight: 600; font-size: 27px; line-height: 30px;
    color: var(--accent); letter-spacing: .2px;
  }
  .postcard--front .contact .name { color: var(--paper); }
  .postcard--back .contact .name { color: var(--ink); }
  .website {
    position: absolute; right: 26px; top: 750px; font-family: "Jost", sans-serif;
    font-size: 17px; letter-spacing: 1px;
  }
  .postcard--front .website { color: var(--paper); }
  .postcard--back .website { color: var(--ink); }

  .stamp-box { position: absolute; left: 37px; top: 535px; width: 135px; height: 135px; border: 1px solid var(--rule); }
  .address-line { position: absolute; left: 196px; width: 314px; height: 1px; background: var(--rule); }
</style>
</head>
<body>

<section class="postcard postcard--front">
  <div class="hero-photo" role="img" aria-label="Photo of two roofers in hard hats repairing shingles on a house roof"></div>
  <svg class="shape" width="538" height="808" viewBox="0 0 538 808">
    <path d="M0,808 L0,395 Q0,335 55,310 L240,178 Q269,160 298,178 L483,310 Q538,335 538,395 L538,808 Z" fill="var(--ink)"/>
  </svg>
  <div class="brand-mark"><span class="dot"></span>LARK ROOFING</div>
  <div class="headline headline--top">POST STORM</div>
  <div class="headline headline--bottom">REPAIR SPECIAL</div>
  <div class="damage-photos">
    <span class="p1" role="img" aria-label="Close-up of storm-damaged shingles with missing tabs"></span>
    <span class="p2" role="img" aria-label="Roof ridge with lifted shingles"></span>
    <span class="p3" role="img" aria-label="House gable and roof edge after a storm"></span>
  </div>
  <div class="accent-rule"></div>
  <p class="body-copy">After the recent hurricanes, it's very important<br>to have your roof checked and any repairs<br>fixed right away before they become a bigger,<br>more costly problem.</p>
  <div class="contact">
    <div class="name">LARK ROOFING</div>
    <div class="phone">888.417.LARK</div>
  </div>
  <div class="website">www.larkroofing.example</div>
</section>

<section class="postcard postcard--back">
  <svg class="shape" width="538" height="808" viewBox="0 0 538 808">
    <defs>
      <filter id="panel-shadow" x="-10%" y="-10%" width="120%" height="130%">
        <feDropShadow dx="0" dy="10" stdDeviation="10" flood-color="#000" flood-opacity=".3"/>
      </filter>
    </defs>
    <path d="M0,0 L538,0 L538,340 Q538,372 505,390 L305,488 Q269,505 233,488 L33,390 Q0,372 0,340 Z" fill="var(--ink)" filter="url(#panel-shadow)"/>
  </svg>
  <div class="brand-mark"><span class="dot"></span>LARK ROOFING</div>
  <p class="body-copy">Even though your home wasn't<br>directly hit by the storm, the<br>highest wind gust could've<br>caused unseen damage.</p>
  <div class="accent-rule"></div>
  <div class="stamp-box"></div>
  <div class="address-line" style="top:580px"></div>
  <div class="address-line" style="top:625px"></div>
  <div class="address-line" style="top:668px"></div>
  <div class="contact">
    <div class="name">LARK ROOFING</div>
    <div class="phone">888.417.LARK</div>
  </div>
  <div class="website">www.larkroofing.example</div>
</section>

</body>
</html>
```